Brindlecove.io - Please redesign to make it look better from current design

We already have the current website, that you can access but we think it can improve from current version.
Brindlecove is a cryptocurrency hedge fund that allow you to participate in the hedge fund with cryptocurrency such as eth.
At current phase, we are doing an ICO, then we want to make sure that the website it looks professional, beautiful and trustable enough for investors after looking at our website.
Target Market(s)
Investors
Industry/Entity Type
Investment
Coding
Coded - Design and coding required
Number of Pages Required
1 page
Look and feel

```html
<!DOCTYPE html>
<html lang="en">
<head>
<meta charset="utf-8">
<title>Brindlecove Fund – Digital Asset Management</title>
<link rel="stylesheet" href="https://fonts.googleapis.com/css2?family=Roboto:wght@300;400;500&family=Open+Sans:ital,wght@0,400;0,600;0,700;1,400&display=swap">
<style>
:root{
  --navy:#15238c;
  --ice:#c9eefc;
  --grey-bg:#eeeeee;
  --rule:#d4d4d4;
  --text:#4a4a4a;
  --white:#ffffff;
}
*{margin:0;padding:0;box-sizing:border-box}
html,body{width:1200px;height:2908px;overflow:hidden}
body{position:relative;background:var(--white);font-family:"Open Sans",sans-serif;color:var(--text)}
.abs{position:absolute}
.heading{font-family:"Roboto",sans-serif;font-weight:300;color:var(--navy)}

/* header */
.brand{left:78px;top:44px;display:flex;align-items:center;gap:12px}
.brand-dot{width:40px;height:40px;border-radius:50%;background:var(--navy)}
.brand-name{font-family:"Roboto",sans-serif;font-size:22px;font-weight:500;color:var(--navy)}
.nav{top:52px;left:0;width:1200px;font-family:"Roboto",sans-serif;font-size:17px;color:#111}
.nav a{position:absolute;color:#111;text-decoration:none}

/* hero */
.hero-title{left:78px;top:246px;font-size:68px;letter-spacing:-1px;white-space:nowrap}
.hero-sub{left:78px;top:356px;font-size:38px}
.hero-rule{left:78px;top:435px;width:62px;height:2px;background:var(--navy)}
.hero-text{left:78px;top:460px;width:540px;font-size:18px;line-height:27px;color:#333}
.divider{left:78px;top:586px;width:518px;height:1px;background:var(--rule)}
.about-title{left:78px;top:622px;font-size:42px}
.about-text{left:78px;top:686px;width:540px;font-size:15.5px;line-height:25px;color:#444}
.btn-primary{left:78px;top:912px;width:164px;height:48px;background:var(--navy);color:var(--white);font-size:15px;font-weight:700;display:flex;align-items:center;justify-content:center}
.hero-art{left:660px;top:126px;width:525px;height:885px;background:radial-gradient(circle at 50% 45%,#e4e8f8 0%,#f4f6fc 60%,#ffffff 100%);border-radius:8px}

/* team */
.team{left:0;top:1065px;width:1200px;height:565px;background:var(--navy)}
.team-title{left:0;top:1112px;width:1200px;text-align:center;font-size:42px;color:var(--white)}
.card{top:1183px;width:322px;height:384px;background:var(--white)}
.card-head{position:absolute;left:0;top:0;width:100%;height:120px;border-bottom:1px solid #dcdcdc}
.card-photo{position:absolute;left:12px;top:18px;width:86px;height:86px;border-radius:50%;background:linear-gradient(160deg,#8a6c5c,#3d3336)}
.card-role{position:absolute;left:110px;top:30px;font-size:15px;font-style:italic;color:#222}
.card-name{position:absolute;left:110px;top:56px;font-family:"Roboto",sans-serif;font-size:18px;color:var(--navy);white-space:nowrap}
.card-bio{position:absolute;left:14px;top:138px;width:298px;font-size:14.5px;line-height:22.5px;color:#555}

/* process */
.process{left:0;top:1630px;width:1200px;height:413px;background:var(--grey-bg)}
.process-title{left:78px;top:1674px;font-size:42px}
.process-sub{left:78px;top:1762px;font-size:28px;font-weight:400}
.process-text{left:78px;top:1812px;width:510px;font-size:15.5px;line-height:25px;color:#555}
.process-art{left:679px;top:1717px;width:330px;height:223px;background:linear-gradient(135deg,#2a3aa0,var(--navy));border-radius:6px;opacity:.9}

/* distribution */
.dist-title{left:0;top:2090px;width:1200px;text-align:center;font-family:"Roboto",sans-serif;font-weight:400;font-size:29px;color:var(--navy)}
.dist-label{font-size:19px;color:#222;line-height:22px;white-space:nowrap}
.dist-label small{font-size:15px}
.dist-label span{display:block;font-size:15px;color:#444}
.dist-centre{text-align:center}
.dist-note{left:0;top:2478px;width:1200px;text-align:center;font-size:17px;color:#222}

/* footer */
.footer{left:0;top:2555px;width:1200px;height:353px;background:var(--navy)}
.foot-h{top:2594px;font-family:"Roboto",sans-serif;font-weight:400;font-size:21px;color:var(--white)}
.foot-text{font-size:15px;line-height:25px;color:var(--white)}
.btn-pdf{left:78px;top:2751px;width:166px;height:52px;background:var(--ice);color:var(--navy);font-size:15px;font-weight:700;display:flex;align-items:center;justify-content:center}
.contact-brand{left:355px;top:2636px;display:flex;align-items:center;gap:12px;font-family:"Roboto",sans-serif;font-size:20px;letter-spacing:1px;color:var(--white)}
.address{left:388px;top:2677px;width:240px;font-size:15px;line-height:25px;color:var(--white)}
.news-input{left:640px;top:2722px;width:220px;height:51px;background:var(--white);font-size:14px;color:#888;padding-left:22px;display:flex;align-items:center}
.news-btn{left:860px;top:2722px;width:50px;height:51px;background:var(--ice);display:flex;align-items:center;justify-content:center}
.foot-brand{left:960px;top:2640px;width:140px;text-align:center}
.foot-brand .dot{width:56px;height:56px;border-radius:50%;background:var(--white);margin:0 auto 10px}
.foot-brand .name{font-family:"Roboto",sans-serif;font-size:17px;color:var(--white)}
.social{top:2749px;width:42px;height:42px;border-radius:50%;border:2px solid var(--white)}
.social.fill{background:var(--ice);border-color:var(--ice)}
.foot-rule{left:78px;top:2846px;width:1044px;height:1px;background:#3747a3}
.copyright{left:0;top:2866px;width:1200px;text-align:center;font-size:16px;color:var(--white)}
.copyright b{font-weight:700}
</style>
</head>
<body>

<header>
  <div class="abs brand"><span class="brand-dot"></span><span class="brand-name">Brindlecove Fund</span></div>
  <nav class="abs nav">
    <a style="left:640px">Home</a>
    <a style="left:733px">About</a>
    <a style="left:825px">Process</a>
    <a style="left:935px">Our Team</a>
    <a style="left:1057px">Contact</a>
  </nav>
</header>

<section>
  <h1 class="abs heading hero-title">Brindlecove Fund</h1>
  <h2 class="abs heading hero-sub">Digital Asset Management</h2>
  <div class="abs hero-rule"></div>
  <p class="abs hero-text">BrindlecoveFund enable companies and investors to facilities business operation in modern digital world, including asset management on hedge fund strategy model.</p>
  <div class="abs divider"></div>
  <h2 class="abs heading about-title">ABOUT US</h2>
  <p class="abs about-text">BrindlecoveFund process and manages on hedge fund strategy models which invests in a diversified portfolio of blockchain tokens. Blockchain tokens are emerging which add a monetary incentive layer to p2p protocols and facilitate equity crowdfunding that anyone in the world can participate in. This means open source software developers can monetize their networks at the protocol level and users of the network are the equity owners of the network. For this conditions, returns will go to holders of the tokens.</p>
  <div class="abs btn-primary">EXPLORE MORE</div>
  <div class="abs hero-art" role="img" aria-label="Line illustration of connected crypto icons: coin, rocket, key, chart, padlock, wallet, payment window and blocks"></div>
</section>

<section>
  <div class="abs team"></div>
  <h2 class="abs heading team-title">EXECUTIVE TEAM</h2>

  <article class="abs card" style="left:78px">
    <div class="card-head">
      <div class="card-photo" role="img" aria-label="Portrait photo of the director"></div>
      <div class="card-role">Director</div>
      <div class="card-name">Kittipat Wongsaree</div>
    </div>
    <p class="card-bio">As a hedge fund manager. Wongsaree is the Chief Executive Officer of Thornbury Capital LLC, an investment manager of Greyhaven Metal Fund SP (Long-Short Equity Fund, investing in U.S. Stock Market) and Kestrel Ridge Fund (Managed Futures Fund, focusing in Japanese Futures Market) Both based in Tokyo.</p>
  </article>

  <article class="abs card" style="left:438px">
    <div class="card-head">
      <div class="card-photo" role="img" aria-label="Portrait photo of the technical advisor" style="background:linear-gradient(160deg,#c9d1c0,#5d6150)"></div>
      <div class="card-role">Technical advisor</div>
      <div class="card-name">Narathip Kaewsri</div>
    </div>
    <p class="card-bio">Kaewsri has various experienced on cryptocurrency and blockchain technology. He created what was the world's 4th most valuable cryptocurrency in February 2014. He is also the world's first person to implement stealth addresses in QX-Purses, improving cryptocurrency anonymity.</p>
  </article>

  <article class="abs card" style="left:799px">
    <div class="card-head">
      <div class="card-photo" role="img" aria-label="Portrait photo of the marketing consultant" style="background:linear-gradient(160deg,#9a5a3e,#3a2320)"></div>
      <div class="card-role">Marketing Consultant</div>
      <div class="card-name">Chanawut Pornsiriwat</div>
    </div>
    <p class="card-bio">Pornsiriwat embeds a decade of experience in brand building, strategic planning, and marketing communication across the global agencies, such as Halvard Worldgroup, NVRA, Oren Bassett, Kuramodo. His seasoned specialty focuses on exploring a new market insight to formulate disruptive strategies</p>
  </article>
</section>

<section>
  <div class="abs process"></div>
  <h2 class="abs heading process-title">PROCESS</h2>
  <h3 class="abs heading process-sub">Hedge Fund Model</h3>
  <p class="abs process-text">BrindlecoveFund run on closed-end fund (CEF) model which offers its shares to investors and utilize the fund to speculate and invest in the innovative blockchain tokens. BrindlecoveFund will charge an upfront annual operation fee 4% of the money raised during the ICO. After that, the fund will charge a quarterly performance of 50% on the net profit made.</p>
  <div class="abs process-art" role="img" aria-label="Illustration of gears beside a rising dollar chart"></div>
</section>

<section>
  <h2 class="abs dist-title">Net Profit Distribution</h2>
  <svg class="abs" style="left:0;top:2140px" width="1200" height="330" viewBox="0 2140 1200 330">
    <g fill="none" stroke="#cfcfcf" stroke-width="1.5">
      <polyline points="515,2302 440,2272 215,2272"/>
      <polyline points="687,2302 762,2272 1005,2272"/>
      <polyline points="548,2403 480,2435 245,2435"/>
      <polyline points="654,2403 722,2435 985,2435"/>
      <line x1="601" y1="2240" x2="601" y2="2196"/>
      <line x1="460" y1="2196" x2="740" y2="2196"/>
    </g>
    <polygon points="601,2240 687,2302 654,2403 548,2403 515,2302" fill="var(--ice)"/>
    <g fill="var(--navy)">
      <circle cx="601" cy="2240" r="4"/><circle cx="687" cy="2302" r="4"/>
      <circle cx="654" cy="2403" r="4"/><circle cx="548" cy="2403" r="4"/>
      <circle cx="515" cy="2302" r="4"/>
    </g>
    <text x="601" y="2335" text-anchor="middle" font-family="Roboto, sans-serif" font-size="17" font-weight="500" fill="var(--navy)">Brindlecove</text>
  </svg>

  <div class="abs dist-label dist-centre" style="left:400px;top:2146px;width:402px">50 %<span>of net profit is distributed to investors</span></div>
  <div class="abs dist-label" style="left:213px;top:2210px">0 – 5 % <small>net profit</small> &gt; 0%<span>performance fee</span></div>
  <div class="abs dist-label" style="left:784px;top:2210px">&gt; 15% <small>net profit</small> &gt; 15%<span>performance fee</span></div>
  <div class="abs dist-label" style="left:252px;top:2378px">5 – 10% <small>net profit</small> &gt; 5%<span>performance fee</span></div>
  <div class="abs dist-label" style="left:747px;top:2378px">10-15 % <small>net profit</small> &gt; 13%<span>performance fee</span></div>
  <p class="abs dist-note">The remainder (50% minus performance fee, so at least 35%) is reinvested</p>
</section>

<footer>
  <div class="abs footer"></div>

  <h4 class="abs foot-h" style="left:80px">FOR MORE INFO</h4>
  <p class="abs foot-text" style="left:80px;top:2636px;width:240px">Lorem Ipsum is simply dummy text of the printing and typesetting industry. Lorem Ipsum has been the industry's.</p>
  <div class="abs btn-pdf">DOWNLOAD PDF</div>

  <h4 class="abs foot-h" style="left:355px">CONTACT INFO</h4>
  <div class="abs contact-brand">
    <svg width="20" height="26" viewBox="0 0 20 26"><path d="M10 0C4.5 0 0 4.4 0 9.8 0 17 10 26 10 26s10-9 10-16.2C20 4.4 15.5 0 10 0z" fill="#fff"/><circle cx="10" cy="9.5" r="3.8" fill="var(--navy)"/></svg>
    <span>Brindlecove Fund</span>
  </div>
  <p class="abs address">Rooms 08-12, 9B/F, East Tower, Meridian Trade Centre, Lantern Bay, 42, Ferry Road, Harbourside, Kowloon, Hong Kong.</p>

  <h4 class="abs foot-h" style="left:640px">NEWSLETTER</h4>
  <p class="abs foot-text" style="left:640px;top:2636px;width:260px">Subscribe to Our Newsletter to get latest News &amp; Updates About Company</p>
  <div class="abs news-input">Enter Your E-Mail</div>
  <div class="abs news-btn">
    <svg width="24" height="24" viewBox="0 0 24 24"><path d="M2 11 22 2 15 22 11 13z" fill="none" stroke="var(--navy)" stroke-width="2" stroke-linejoin="round"/><path d="M11 13 22 2" stroke="var(--navy)" stroke-width="2"/></svg>
  </div>

  <div class="abs foot-brand"><div class="dot"></div><div class="name">Brindlecove Fund</div></div>
  <span class="abs social fill" style="left:957px"></span>
  <span class="abs social" style="left:1007px"></span>
  <span class="abs social" style="left:1057px"></span>

  <div class="abs foot-rule"></div>
  <p class="abs copyright">© <b>brindlecove fund</b> - 2017. All Rights Reserved.</p>
</footer>

</body>
</html>
```